Introduction of new dentist and new treatments

We want inform our Patients of our new dentist and new treatment methods. It is dealing about biologic dentistry and holistic dentistry. we are in switzerland and speak german

Font styles to use
Sans Serif

Colors
00a990
33b8a4
9bcb3c
acd036
cadf82
0292cd
3176b5
e34297
e667a6

Requirements
Must have
• Text, which can be edited. It will be in german
• Name of the dental clinic is
• "Brivana - Ihr Zahnarzt in Zug"
Nice to have
• A4 Layout

```html
<!DOCTYPE html>
<html lang="de">
<head>
<meta charset="utf-8">
<title>Brivana – Interdisziplinäre Zahnmedizin</title>
<link rel="stylesheet" href="https://fonts.googleapis.com/css2?family=Barlow:wght@400;500;600;700&display=swap">
<style>
  :root {
    --green: #9bcb3c;
    --green-soft: #b9d67a;
    --green-tint: #f6f9ee;
    --blue: #0292cd;
    --navy: #1b2a6b;
    --text: #454545;
    --white: #ffffff;
    --backdrop: #e9ebef;
  }
  * { box-sizing: border-box; margin: 0; padding: 0; }
  html, body {
    width: 1200px; height: 1200px; overflow: hidden;
    background: var(--backdrop);
    font-family: "Barlow", sans-serif;
  }
  .page {
    position: absolute; left: 190px; top: 20px;
    width: 820px; height: 1160px;
    background: var(--white);
    box-shadow: 0 4px 18px rgba(0,0,0,.12);
    overflow: hidden;
  }
  .title-line {
    position: absolute; left: 50px;
    background: var(--green); color: var(--white);
    font-weight: 500; font-size: 74px; line-height: 71px;
    padding: 0 2px; letter-spacing: -0.5px;
  }
  .title-line.first { top: 83px; }
  .title-line.second { top: 163px; }
  .subtitle {
    position: absolute; left: 50px; top: 250px;
    color: var(--blue); font-weight: 500;
    font-size: 28px; line-height: 34px;
  }
  .brand {
    position: absolute; left: 548px; top: 240px; width: 230px;
    text-align: center; color: var(--navy);
  }
  .brand-name { font-size: 28px; font-weight: 500; letter-spacing: 6px; }
  .brand-tagline { font-size: 13px; font-weight: 500; margin-top: 6px; }
  .intro {
    position: absolute; left: 50px; top: 402px;
    width: 520px; height: 128px;
    background: var(--green-tint);
    padding: 18px 60px 0 22px;
  }
  .intro h2 { color: var(--green); font-size: 18px; font-weight: 700; margin-bottom: 10px; }
  .intro p { color: var(--text); font-size: 13px; line-height: 18px; text-align: justify; }
  .portrait {
    position: absolute; left: 547px; top: 342px;
    width: 224px; height: 224px; border-radius: 50%;
    border: 4px solid var(--green-soft);
    background: radial-gradient(circle at 50% 40%, #c9c9c9, #9a9a9a 70%, #2e6fb8 100%);
  }
  .section { position: absolute; width: 352px; }
  .section.col-left { left: 50px; }
  .section.col-right { left: 418px; }
  .section-head { display: flex; align-items: stretch; gap: 3px; margin-bottom: 8px; }
  .section-head .marker {
    flex: 0 0 30px; height: 30px; background: var(--green);
    display: flex; align-items: center; justify-content: center;
  }
  .section-head h3 {
    flex: 1; background: var(--blue); color: var(--white);
    font-size: 14px; font-weight: 700; line-height: 16px;
    text-transform: uppercase; padding: 6px 8px;
  }
  .section p { color: var(--text); font-size: 13px; line-height: 18px; text-align: justify; }
  .footer-line { position: absolute; left: 55px; top: 1114px; width: 716px; height: 5px; background: var(--green); }
  .footer-band { position: absolute; left: 55px; top: 1119px; width: 716px; height: 41px; background: var(--blue); }
</style>
</head>
<body>
<main class="page">
  <h1>
    <span class="title-line first">Interdisziplinäre</span>
    <span class="title-line second">Zahnmedizin</span>
  </h1>
  <p class="subtitle">Zusammenhang zwischen<br>Zahnproblemen und der<br>Gesundheit von Körper und Geist</p>

  <div class="brand">
    <div class="brand-name">BRIVANA</div>
    <div class="brand-tagline">Ihr Zahnarzt in Zug</div>
  </div>

  <section class="intro">
    <h2>Zahn und Gesundheit haben eins gemeinsam</h2>
    <p>Man vermisst sie, wenn sie fehlt. Zähne haben einen engen Zusammenhang zur Gesundheit und können diese beeinflussen. Sowohl negativ als auch positiv.</p>
  </section>
  <div class="portrait" role="img" aria-label="Porträtfoto des neuen Zahnarztes im blauen Poloshirt"></div>

  <section class="section col-left" style="top:593px">
    <div class="section-head">
      <span class="marker"><svg width="12" height="14" viewBox="0 0 12 14"><path d="M3 2l6 5-6 5" fill="none" stroke="#fff" stroke-width="2.5"/></svg></span>
      <h3>Funktion des Kauorgans und interdisziplinäre Zahnmedizin</h3>
    </div>
    <p>„Funktion ist nicht alles. Aber ohne Funktion ist alles nichts!“ Sagte einst Prof. A. Kellner (Zahnarzt, Gnathologie) und betonte die Bedeutung der Funktion des Kausystems. Sprechen, Kauen aber auch Körperhaltung und Stressmanagement gehören zu den Funktionen der Zähne. Ein gut funktionierendes Kauorgan (nach Prof. R. Marten, interdisziplinäre Zahnmedizin) kann Stress bewältigen und mehr Leistung und Wohlbefinden bringen. Sehr oft erkennt man Funktionsstörungen daran, dass die Zähne nicht richtig zueinander passen oder Muskelverspannungen und Schmerzen im Kiefergelenk auftreten.</p>
  </section>

  <section class="section col-left" style="top:869px">
    <div class="section-head">
      <span class="marker"><svg width="12" height="14" viewBox="0 0 12 14"><path d="M3 2l6 5-6 5" fill="none" stroke="#fff" stroke-width="2.5"/></svg></span>
      <h3>Parodontitis und systemische Erkrankungen</h3>
    </div>
    <p>Parodontitis (Entzündung des Zahnhalteapparats) ist eine der häufigsten chronischen Krankheiten weltweit und daher gut erforscht. Herzkrankheiten, Diabetes und Frühgeburtlichkeit sind einige der systemischen Krankheiten mit der Parodontitis in Zusammenhang steht. Zahnfleischbluten, Zahnlockerung, Zahnfleischschwund und Zahnverlust sind typische Begleiterscheinungen von Parodontitis. Eine systematische Parodontitis-Behandlung kann auch positive Auswirkungen auf die gesamte Gesundheit haben.</p>
  </section>

  <section class="section col-right" style="top:598px">
    <div class="section-head">
      <span class="marker"><svg width="12" height="14" viewBox="0 0 12 14"><path d="M3 2l6 5-6 5" fill="none" stroke="#fff" stroke-width="2.5"/></svg></span>
      <h3>Zahnverlust und neurologische Auswirkung</h3>
    </div>
    <p style="margin-top:14px">Ein physiologisches Kausystem hat sehr feine Steuerungs- und Wahrnehmungsmöglichkeiten. Bei Zahnverlust werden diese Fähigkeiten weniger benötigt. Weniger gebrauchte Ressourcen werden von der Natur dementsprechend abgebaut. Studien zeigen, dass Menschen mit weniger Zähnen mehr Risiko zur Bildung von Demenz bergen.</p>
  </section>

  <section class="section col-right" style="top:814px">
    <div class="section-head">
      <span class="marker"><svg width="12" height="14" viewBox="0 0 12 14"><path d="M3 2l6 5-6 5" fill="none" stroke="#fff" stroke-width="2.5"/></svg></span>
      <h3>Ganzheitliche Erklärungen</h3>
    </div>
    <p style="margin-top:16px">Die komplementäre Zahnheilkunde, sehr oft auch als ganzheitliche oder biologische Zahnheilkunde bezeichnet, versucht mit Hilfe von Meridianen (Traditionelle Chinesische Medizin), den Zusammenhang zwischen Zähnen und anderen Organen und Körperteilen zu erklären. Es gibt immer mehr Patienten und Zahnärzte die von dieser Theorie und deren Ergebnissen überzeugt sind. Aufgrund der wissenschaftlichen Lage ist eine ausführliche Aufklärung vor der Behandlung sehr ratsam.</p>
  </section>

  <div class="footer-line"></div>
  <div class="footer-band"></div>
</main>
</body>
</html>
```